Business Card Design Project

Need a business card which is crisp, clear and modern.
with the logo being highlighted and at the back of the card our services.
Please use the attached logo for creating the cards.

Reason: need to receive some good designs

Target Market(s)

Our target customers will be hotels, offices, single users

Industry/Entity Type

Business

```html
<!DOCTYPE html>
<html lang="en">
<head>
<meta charset="utf-8">
<title>Joinwell Business Card</title>
<link href="https://fonts.googleapis.com/css2?family=Open+Sans:wght@400;600;700&display=swap" rel="stylesheet">
<style>
  :root{
    --bg:#262626;
    --card:#ffffff;
    --ink:#1d1d1f;
    --green:#0d9b48;
    --blue:#16a5e6;
    --navy:#1b4f8c;
    --orange:#f08a1c;
    --red:#e1261c;
  }
  *{margin:0;padding:0;box-sizing:border-box}
  html,body{width:1200px;height:1200px;overflow:hidden;background:var(--bg)}
  body{font-family:"Open Sans",Arial,sans-serif;color:var(--ink);position:relative}
  .card{position:absolute;left:150px;width:900px;height:514px;background:var(--card);overflow:hidden;box-shadow:0 14px 30px rgba(0,0,0,.45)}
  .card--front{top:58px}
  .card--back{top:628px}
  .bands{position:absolute;inset:0;width:900px;height:514px}
  .brand{display:flex;align-items:center;gap:18px;position:absolute;font-weight:700;color:var(--ink);letter-spacing:1px}
  .brand__mark{background:var(--green);border-radius:50%}
  .card--front .brand{left:220px;top:168px;font-size:110px}
  .card--front .brand__mark{width:70px;height:70px}
  .card--back .brand{left:56px;top:44px;font-size:56px}
  .card--back .brand__mark{width:38px;height:38px}
  .person{position:absolute;right:70px;top:52px;text-align:right}
  .person__name{font-size:40px;color:var(--blue);line-height:1.05}
  .person__title{font-size:22px;color:var(--ink)}
  .address{position:absolute;left:60px;top:210px;font-size:21px;line-height:1.3}
  .contacts{position:absolute;left:60px;top:300px;list-style:none;font-size:21px}
  .contacts li{display:flex;align-items:center;gap:16px;height:34px}
  .contacts svg{width:26px;height:24px}
  .web{position:absolute;right:36px;bottom:30px;color:#fff;font-size:20px;letter-spacing:4px;font-weight:600}
</style>
</head>
<body>

<section class="card card--front" aria-label="Card front">
  <div class="brand"><span class="brand__mark"></span>Joinwell</div>
  <svg class="bands" viewBox="0 0 900 514" aria-hidden="true">
    <rect x="0" y="432" width="900" height="46" fill="var(--green)"/>
    <rect x="0" y="488" width="900" height="14" fill="var(--blue)"/>
  </svg>
</section>

<section class="card card--back" aria-label="Card back">
  <svg class="bands" viewBox="0 0 900 514" aria-hidden="true">
    <polygon points="0,462 560,462 598,404 612,404 574,474 0,474" fill="var(--blue)"/>
    <polygon points="0,486 586,486 628,412 900,412 900,514 0,514" fill="var(--green)"/>
  </svg>
  <div class="brand"><span class="brand__mark"></span>Joinwell</div>
  <div class="person">
    <div class="person__name">Your Name</div>
    <div class="person__title">Title</div>
  </div>
  <p class="address">1275 Harbor Point Ave, Suite 4<br>Lindale, CA 94821</p>
  <ul class="contacts">
    <li><svg viewBox="0 0 26 24"><rect width="26" height="24" rx="4" fill="var(--navy)"/><path d="M8 5c-2 1-2 4 0 8s5 6 7 6l2-2-3-3-2 1c-1-1-2-3-3-4l1-2-2-4z" fill="#fff"/></svg>000 000 00</li>
    <li><svg viewBox="0 0 26 24"><rect x="2" y="1" width="22" height="22" rx="3" fill="none" stroke="var(--orange)" stroke-width="2.5"/><rect x="6" y="5" width="14" height="4" fill="var(--orange)"/><g fill="var(--orange)"><rect x="6" y="12" width="3" height="3"/><rect x="11" y="12" width="3" height="3"/><rect x="16" y="12" width="3" height="3"/><rect x="6" y="17" width="3" height="3"/><rect x="11" y="17" width="3" height="3"/><rect x="16" y="17" width="3" height="3"/></g></svg>000 000 00</li>
    <li><svg viewBox="0 0 26 24"><rect x="1" y="4" width="24" height="16" fill="var(--red)"/><path d="M1 4l12 9 12-9" fill="none" stroke="#fff" stroke-width="1.5"/></svg>username@joinwell.com</li>
  </ul>
  <div class="web">www.joinwell.com</div>
</section>

</body>
</html>
```